Advertisement Design Project

PLEASE SEE DIMENSION REQUIREMENTS:
Ad size is: 3 3/8" x 9 1/2"
Full color
Output to PDF File (press optimized, CMYK, fonts embedded, 300 dpi).

I am looking for a full-color advertisement for a professional guide that is printed annually. I am a law firm servicing the LGBT community in the greater Seattle, Washington, USA area.

I have attached a mock-up idea similar to what I'd like, but I am open to different design elements and copy. The copy should at the very least list the broad legal practice areas I have mentioned.

The final deisgn should be simple, elegant, and convey that my law firm is the trusted choice for LGBT individuals, families and small businesses.

I've uploaded my logo and some of the original photo elements.

Thank you!

Reason: I've seen so many great designs that I need another day to follow-up with everyone. Thank you very much for your submissions!

Target Market(s)

LGBT individuals and families in need of legal services.

Industry/Entity Type

Law Firm

Requirements
Must have
• It must have our logo, web address, phone number, and email address.

```html
<!DOCTYPE html>
<html lang="en">
<head>
<meta charset="utf-8">
<title>Prismwell Law PS – Advertisement</title>
<link href="https://fonts.googleapis.com/css2?family=Questrial&family=Mulish:wght@800&family=Russo+One&display=swap" rel="stylesheet">
<style>
  :root {
    --frame-outer: #dedede;
    --frame-inner: #c9c9c9;
    --panel-light: #fbfbfb;
    --panel-mid: #ececec;
    --brand-red: #e3232b;
    --body-text: #3a3a3a;
    --contact-text: #666666;
    --name-text: #7a7a7a;
    --photo-top: #b9b3ae;
    --photo-bottom: #6f7075;
  }
  * { margin: 0; padding: 0; box-sizing: border-box; }
  html, body { width: 849px; height: 1200px; overflow: hidden; background: var(--frame-outer); }
  .ad {
    position: relative;
    width: 849px; height: 1200px;
    background: var(--frame-outer);
  }
  .ad-frame {
    position: absolute;
    left: 16px; top: 16px; width: 812px; height: 1158px;
    background: var(--frame-inner);
  }
  .ad-panel {
    position: absolute;
    left: 38px; top: 38px; width: 766px; height: 1112px;
    background: radial-gradient(ellipse at 55% 45%, var(--panel-light) 0%, var(--panel-light) 35%, var(--panel-mid) 100%);
    overflow: hidden;
  }
  .brand {
    position: absolute;
    left: 138px; top: 64px;
    display: flex; align-items: center; gap: 14px;
    color: var(--brand-red);
    font-family: "Questrial", sans-serif;
    font-size: 54px;
    line-height: 1;
    white-space: nowrap;
  }
  .brand-dot {
    width: 58px; height: 58px; border-radius: 50%;
    border: 4px solid var(--brand-red);
  }
  .copy {
    position: absolute;
    left: 75px; top: 203px;
    font-family: "Questrial", sans-serif;
    font-size: 29px;
    letter-spacing: 0.6px;
    line-height: 36px;
    color: var(--body-text);
    white-space: nowrap;
  }
  .copy p { margin-bottom: 30px; }
  .contact {
    position: absolute;
    left: 110px; top: 590px;
    font-family: "Mulish", sans-serif;
    font-weight: 800;
    font-size: 23px;
    line-height: 33px;
    color: var(--contact-text);
    white-space: nowrap;
  }
  .portrait {
    position: absolute;
    left: 10px; top: 692px; width: 395px; height: 420px;
    background: linear-gradient(180deg, var(--photo-top) 0%, var(--photo-bottom) 100%);
  }
  .signature {
    position: absolute;
    left: 437px; top: 985px;
    font-family: "Russo One", sans-serif;
    font-size: 30px;
    line-height: 34px;
    color: var(--name-text);
    white-space: nowrap;
  }
</style>
</head>
<body>
  <div class="ad">
    <div class="ad-frame"></div>
    <div class="ad-panel">
      <div class="brand">
        <span class="brand-dot"></span>
        <span class="brand-name">Prismwell Law PS</span>
      </div>

      <div class="copy">
        <p>Proudly serves as the trusted legal advisor<br>to hundreds of LGBT individuals and families<br>for their estate planning, probate, real estate,<br>and small business needs.</p>
        <p>Contact Prismwell Law PS so that you too can<br>discover unparalleled service and value in the<br>delivery of legal services.</p>
        <p>Because you should trust your attorney.</p>
      </div>

      <div class="contact">
        <div>www.prismwell-law.com | (206) 555-0147</div>
        <div>hello@prismwell-law.com</div>
        <div>840 Lakeview Ave #1200 | Seattle, WA 98109</div>
      </div>

      <div class="portrait" role="img" aria-label="Portrait photograph of the attorney in a dark suit and tie"></div>

      <div class="signature">
        Daniel R.Hollis,<br>Attorney<br>&amp; Principal
      </div>
    </div>
  </div>
</body>
</html>
```